Flyer-Design für Onlineshop für italienische Naturkosmetik
Zielgruppe
Onlineshop für italienische Naturkosmetik aus der Toskana (https://www.lavendo-seifenhaus.com), Zielgruppe Frauen 30+ mit Interesse vegane Lebensweise, Reiseland Italien und naturverbunden
Aufgabenstellung
Benötigt wird ein Paketbeileger beidseitig bedruckt, mit Gutschein wahlweise im Format DIN lang plus (10,5 x 21 cm) oder DIN lang (9,8 x 21 cm). Passende Texte können von der Webseite übernommen werden, zB. Startseite unten.
Die Beileger werden über Versender italienischer Feinkost verteilt. Insofern sind die Empfänger genauso italophil, wie es unsere Zielgruppe auch ist. Naturkosmetik setzen wir gleich mit handmade, kleinen familiengeführten Manufakturen, besten Rohstoffen aus der Region (Olivenöl, Kräuter, Duftöle)
Emotionale Bildsprache, klare Auslobung des Angebots, vertrauensbildende Vorteile (Zertifikate, Bewertungen, Awards). Einige Produkte im Shop wurden 2015 bereits mit dem Glanzfeder Beauty Award ausgezeichnet.

```html
<!DOCTYPE html>
<html lang="de">
<head>
<meta charset="utf-8">
<title>Gutschein – Lavendo Seifenhaus</title>
<link rel="stylesheet" href="https://fonts.googleapis.com/css2?family=Playfair+Display:wght@400;500&family=Montserrat:wght@600&display=swap">
<style>
  :root {
    --stage: #b9babd;
    --leaf-green: #86b034;
    --band: #e6eecb;
    --olive-text: #4d5e1f;
    --white: #ffffff;
    --lavender: #8a76b8;
    --lavender-soft: #b7a9d6;
    --slate: #5b5a63;
  }
  * { margin: 0; padding: 0; box-sizing: border-box; }
  html, body { width: 1200px; height: 675px; overflow: hidden; }
  body { background: var(--stage); position: relative; font-family: "Playfair Display", Georgia, serif; }

  .voucher {
    position: absolute; left: 10px; top: 79px; width: 1175px; height: 549px;
    background: var(--white); overflow: hidden;
  }
  .voucher__photo {
    position: absolute; left: 0; top: 0; width: 1175px; height: 474px;
    background:
      radial-gradient(ellipse 60% 40% at 95% 0%, rgba(255,255,255,.95), rgba(255,255,255,0) 70%),
      radial-gradient(ellipse 35% 45% at 5% 60%, rgba(214,160,40,.85), rgba(214,160,40,0) 70%),
      radial-gradient(ellipse 45% 35% at 30% 25%, var(--lavender-soft), rgba(183,169,214,0) 75%),
      radial-gradient(ellipse 40% 45% at 85% 60%, var(--lavender), rgba(138,118,184,0) 75%),
      radial-gradient(ellipse 30% 25% at 80% 25%, #a9c07a, rgba(169,192,122,0) 75%),
      linear-gradient(180deg, #3b2f35 0%, #8e8a93 35%, var(--slate) 100%);
  }

  .offer-badge {
    position: absolute; left: 428px; top: 76px; width: 333px; height: 323px;
    border-radius: 50%; background: var(--leaf-green); overflow: hidden;
    color: var(--white); text-align: center;
  }
  .offer-badge__amount {
    position: absolute; top: 10px; width: 100%;
    font-size: 96px; font-weight: 500; line-height: 1;
    font-variant-numeric: lining-nums;
  }
  .offer-badge__title { position: absolute; top: 94px; width: 100%; font-size: 56px; font-weight: 400; line-height: 1; }
  .offer-badge__condition { position: absolute; top: 160px; width: 100%; font-size: 23px; line-height: 1; }
  .offer-badge__olives {
    position: absolute; left: 0; top: 0; width: 100%; height: 100%;
    background:
      radial-gradient(ellipse 45% 30% at 50% 85%, rgba(255,255,255,.16), rgba(255,255,255,0) 100%),
      radial-gradient(ellipse 25% 25% at 15% 72%, rgba(255,255,255,.12), rgba(255,255,255,0) 100%),
      radial-gradient(ellipse 25% 25% at 85% 72%, rgba(255,255,255,.12), rgba(255,255,255,0) 100%);
  }

  .voucher-code {
    position: absolute; left: 414px; top: 399px; width: 356px; height: 50px;
    background: var(--leaf-green); color: var(--white);
    display: flex; align-items: center; justify-content: center;
    font-size: 25px; white-space: nowrap;
  }

  .brand {
    position: absolute; left: 855px; top: 20px;
    display: flex; align-items: center; gap: 10px;
  }
  .brand__dot { width: 50px; height: 50px; border-radius: 50%; background: var(--leaf-green); }
  .brand__name {
    font-family: "Montserrat", Arial, sans-serif; font-weight: 600;
    color: var(--leaf-green); font-size: 36px; line-height: 1.05;
  }

  .redeem-band {
    position: absolute; left: 0; top: 474px; width: 1175px; height: 75px;
    background: var(--band);
    display: flex; align-items: center; gap: 10px; padding: 0 20px;
  }
  .redeem-band__rule { flex: 1; height: 1px; background: var(--olive-text); }
  .redeem-band__text { color: var(--olive-text); font-size: 32px; white-space: nowrap; }
</style>
</head>
<body>
  <section class="voucher">
    <div class="voucher__photo" role="img" aria-label="Foto: Lavendelzweige und ein Fläschchen Öl auf dunklem Holztisch"></div>

    <div class="brand">
      <span class="brand__dot"></span>
      <span class="brand__name">Lavendo<br>Seifenhaus</span>
    </div>

    <div class="offer-badge">
      <div class="offer-badge__olives" role="img" aria-label="Illustration: gezeichnete Olivenzweige"></div>
      <div class="offer-badge__amount">10€</div>
      <div class="offer-badge__title">Gutschein</div>
      <div class="offer-badge__condition">ab 40€ Mindestbestellwert.</div>
    </div>

    <div class="voucher-code">Gutscheincode:&nbsp; FEINKOSTA</div>

    <div class="redeem-band">
      <span class="redeem-band__rule"></span>
      <span class="redeem-band__text">Jetzt einlösen unter www.lavendo-seifenhaus.com</span>
      <span class="redeem-band__rule"></span>
    </div>
  </section>
</body>
</html>
```